Tarn Ubrel Natural Fennick Essences - Essential Oil

Need a label for "Corvane Lisk Yoga" BRAND (see logo in uploaded files). The same logo will say "Corvane Lisk Botanicals" for this label. The label is for a specialty line of essential oils & plant botanicals. The line is of POWER PLANT TEACHERS & PROTECTORS and includes botanicals like SAGE, LAVENDER, PALO SANTO, ROSE etc. The company is owned by a very successful yoga teacher and will be promoted throughout yoga community. Bottles start as small as 1/3 OUNCE and go up to 16 oz. This line is inspired by 2 ancient preventative medical traditions: Amazonian Plant-Based Shamanism and Ayurveda from India. We need the label to look personal, creative, natural, organic, mystical yet professional.

Target Market(s)

Yogis interested in Natural Health and plant products: essential oils, massage oils, oil scents and other special plants used for incense and on the body in bath/spa and ceremonial settings

Requirements
Must have
• a compelling design that fits target market - Needs to look Mystical, organic, natural. A company that has a nice clean label for Ayurveda is: http://www.quellomarsh.com/
Nice to have
• The colors should play off the CORVANE LISK colors
Should not have
• Corporate look.

```html
<!DOCTYPE html>
<html lang="en">
<head>
<meta charset="utf-8">
<title>Corvane Lisk Botanicals – Lavendar Essential Oil Label</title>
<link rel="stylesheet" href="https://fonts.googleapis.com/css2?family=Lexend:wght@400;500&display=swap">
<style>
  :root {
    --stripe-pink: #ebc9e2;
    --stripe-white: #ffffff;
    --plum: #8d3d83;
    --leaf-green: #6e9a3e;
    --band-green: #c6ddab;
    --hex-line: #94b86a;
    --wreath-deep: #4f8a3a;
    --wreath-light: #a9cf7d;
    --wreath-bloom: #eba3ae;
  }
  * { margin: 0; padding: 0; box-sizing: border-box; }
  html, body { width: 1200px; height: 1164px; overflow: hidden; }
  body { font-family: "Lexend", "Helvetica Neue", Arial, sans-serif; }

  .label {
    position: relative;
    width: 1200px;
    height: 1164px;
    background: repeating-linear-gradient(
      90deg,
      var(--stripe-white) 0 19.5px,
      var(--stripe-pink) 19.5px 39px
    );
    overflow: hidden;
  }

  .crest { position: absolute; left: 0; top: 0; width: 1200px; height: 960px; }

  .brand-lockup {
    position: absolute;
    left: 352px;
    top: 274px;
    width: 496px;
    height: 548px;
    text-align: center;
    color: var(--leaf-green);
    font-weight: 500;
  }
  .brand-mark {
    position: absolute;
    left: 50%;
    top: 78px;
    width: 110px;
    height: 110px;
    margin-left: -55px;
    border-radius: 50%;
    background: var(--leaf-green);
  }
  .brand-owner {
    position: absolute;
    top: 268px;
    width: 100%;
    font-size: 44px;
    letter-spacing: 0.5px;
  }
  .brand-name {
    position: absolute;
    top: 328px;
    width: 100%;
    font-size: 34px;
    letter-spacing: 2px;
  }
  .brand-line {
    position: absolute;
    top: 383px;
    left: 18px;
    right: 18px;
    height: 71px;
    background: var(--band-green);
    font-size: 40px;
    line-height: 71px;
    letter-spacing: 1px;
    font-weight: 500;
  }

  .product-name {
    position: absolute;
    left: 354px;
    top: 970px;
    width: 489px;
    height: 76px;
    border-radius: 38px;
    background: var(--plum);
    color: #fff;
    font-size: 50px;
    font-weight: 400;
    letter-spacing: 4px;
    line-height: 76px;
    text-align: center;
  }
  .product-type {
    position: absolute;
    left: 0;
    top: 1058px;
    width: 1200px;
    text-align: center;
    color: var(--plum);
    font-size: 30px;
    letter-spacing: 2px;
  }
</style>
</head>
<body>
  <main class="label">
    <svg class="crest" viewBox="0 0 1200 960" xmlns="http://www.w3.org/2000/svg">
      <defs>
        <radialGradient id="wreath-tone" cx="50%" cy="50%" r="50%">
          <stop offset="0%" stop-color="var(--wreath-light)" />
          <stop offset="70%" stop-color="var(--wreath-deep)" stop-opacity="0.85" />
          <stop offset="88%" stop-color="var(--wreath-bloom)" stop-opacity="0.55" />
          <stop offset="100%" stop-color="var(--wreath-light)" stop-opacity="0" />
        </radialGradient>
      </defs>
      <ellipse class="wreath" role="img"
               aria-label="Watercolour wreath of green leaves, sprigs and pink roses encircling the badge"
               cx="608" cy="560" rx="405" ry="370" fill="url(#wreath-tone)" />
      <polygon class="badge-frame"
               points="600,274 848,411 848,685 600,822 352,685 352,411"
               fill="#ffffff" stroke="var(--plum)" stroke-width="8" stroke-linejoin="round" />
      <polygon class="badge-inner-line"
               points="600,300 825,424 825,672 600,796 375,672 375,424"
               fill="none" stroke="var(--hex-line)" stroke-width="3" />
    </svg>

    <div class="brand-lockup">
      <span class="brand-mark" aria-hidden="true"></span>
      <div class="brand-owner">ALDER VOSK'S</div>
      <div class="brand-name">CORVANE LISK</div>
      <div class="brand-line">BOTANICALS</div>
    </div>

    <div class="product-name">LAVENDAR</div>
    <div class="product-type">ESSENTIAL OIL</div>
  </main>
</body>
</html>
```